Design Our Camera Package Graphic Must Be Awesome! We Have Lots More Work!

We want the attached graphic redesigned to feature our camera packages instead of the the home theater package. The information to be included in the package you can find in the second attachment. We have also included our logo. We want a really nice graphic the winner will have to make 3 graphic all with exact layout but slightly different see our website for an example http://brambleridgefitters.example/home-theater-packages/#.QWTnalKx4rb. Remember this design will be built around the attached file named: Package Graphic info. Your design must standout. If you do really good job we will have a lot more work for you in the future. .

Target Market(s)

Home Owners

Industry/Entity Type

Camera

Font styles to use
Sans Serif

Colors
0255a3
33a6d7
85acd3
3277b5
ffffff

Requirements
Must have
• Pictures of dome cameras and bullet cameras, dvr, our company logo and MUST LOOK AWESOME!
Should not have
• We have included an example of what we are not looking for

```html
<!DOCTYPE html>
<html lang="en">
<head>
<meta charset="utf-8">
<title>Surveillance Packages</title>
<link href="https://fonts.googleapis.com/css2?family=Archivo+Narrow:wght@400;700&family=Oswald:wght@500;700&display=swap" rel="stylesheet">
<style>
  :root{
    --page:#3a3a3a;
    --card:#eceef0;
    --frame:#9a9da1;
    --sky:#c9d3dc;
    --house:#d8cdb6;
    --lawn:#6f7d4a;
    --stripe:#7a4a1f;
    --ink:#1e1e1e;
    --dot:#c0281c;
    --orange:#e8541c;
    --orange-dark:#c23c0e;
    --red:#a8221b;
    --red-dark:#7e1410;
    --peach:#fbd7b8;
    --badge:#3b2420;
    --gold:#c9a06a;
    --brand:#4a3326;
    --white:#ffffff;
  }
  *{box-sizing:border-box;margin:0;padding:0}
  html,body{width:1200px;height:1077px;overflow:hidden;background:var(--page)}
  .flyer{position:absolute;left:40px;top:94px;width:1120px;height:889px;background:var(--card);
    box-shadow:0 6px 24px rgba(0,0,0,.5);font-family:"Archivo Narrow",Arial,sans-serif;color:var(--ink)}
  .frame{position:absolute;left:46px;top:30px;width:1010px;height:859px;border:3px solid var(--frame);
    border-bottom:none;border-radius:22px 22px 0 0;background:var(--white);overflow:hidden}
  .hero{position:absolute;left:0;top:0;width:100%;height:300px;
    background:linear-gradient(180deg,var(--sky) 0%,var(--house) 30%,var(--house) 62%,var(--lawn) 100%)}
  .swoosh{position:absolute;left:0;top:190px;width:100%;height:180px}
  .badge{position:absolute;left:99px;top:-14px;width:282px;height:146px}
  .badge-title{position:absolute;left:0;width:100%;text-align:center;font-family:Oswald,sans-serif;
    color:var(--gold);text-transform:uppercase;letter-spacing:1px}
  .cameras{position:absolute;left:404px;top:312px;width:370px;height:92px;border-radius:46px;
    background:radial-gradient(circle at 50% 40%,#7b7f85,#3e4247)}
  .dvr{position:absolute;left:480px;top:416px;width:231px;height:53px;border-radius:6px;
    background:linear-gradient(180deg,#5a5d61,#1f2124)}
  .brand{position:absolute;left:58px;top:400px;display:flex;align-items:center;gap:10px;
    font-size:30px;font-weight:700;color:var(--brand)}
  .brand-mark{width:22px;height:22px;background:var(--brand)}
  .panel{position:absolute;top:508px;height:338px;border-radius:12px;padding:30px 20px 10px;z-index:1;
    background:linear-gradient(180deg,var(--white) 55%,var(--peach) 100%);box-shadow:0 2px 8px rgba(0,0,0,.25)}
  .panel-basic{left:58px;width:480px}
  .panel-full{left:554px;width:492px}
  .price{position:absolute;top:464px;width:219px;height:52px;border-radius:6px 6px 0 0;z-index:3;
    display:flex;align-items:center;justify-content:center;
    color:var(--white);font-weight:700;font-size:44px;line-height:1}
  .price-cents{font-size:22px;position:relative;top:-12px;margin-left:1px}
  .price-basic{left:185px;background:linear-gradient(180deg,var(--orange),var(--orange-dark))}
  .price-full{left:693px;background:linear-gradient(180deg,var(--red),var(--red-dark))}
  .package-title{font-size:18px;font-weight:700;text-transform:uppercase}
  .list-head{font-size:16px;font-weight:700;margin-top:4px}
  .list{list-style:none;font-size:15.5px;line-height:19px}
  .list li{padding-left:14px;position:relative}
  .list li::before{content:"";position:absolute;left:2px;top:7px;width:6px;height:6px;border-radius:50%;background:var(--dot)}
</style>
</head>
<body>
<div class="flyer">
  <div class="frame">
    <div class="hero" role="img" aria-label="Photo of a two-storey suburban house with porch, dark shutters and lawn"></div>
    <svg class="swoosh" viewBox="0 0 1010 180" preserveAspectRatio="none" aria-hidden="true">
      <path d="M0 180 L0 120 Q500 -10 1010 20 L1010 180 Z" fill="var(--stripe)"/>
      <path d="M0 180 L0 132 Q500 6 1010 34 L1010 180 Z" fill="var(--white)"/>
    </svg>
  </div>

  <div class="badge">
    <svg width="282" height="146" viewBox="0 0 282 146" aria-hidden="true">
      <polygon points="0,73 40,48 40,98" fill="var(--red-dark)"/>
      <polygon points="282,73 242,48 242,98" fill="var(--red-dark)"/>
      <rect x="30" y="10" width="222" height="126" rx="24" fill="var(--badge)" stroke="var(--gold)" stroke-width="4"/>
    </svg>
    <div class="badge-title" style="top:40px;font-size:28px;font-weight:700">Surveillance</div>
    <div class="badge-title" style="top:78px;font-size:22px;font-weight:500">Packages</div>
  </div>

  <div class="cameras" role="img" aria-label="Four grey dome security cameras"></div>
  <div class="dvr" role="img" aria-label="Black digital video recorder unit"></div>

  <div class="brand"><span class="brand-mark"></span>Bramble Ridge Fitters</div>

  <div class="price price-basic">$399<span class="price-cents">99</span></div>
  <div class="price price-full">$999<span class="price-cents">99</span></div>

  <section class="panel panel-basic">
    <h2 class="package-title">4 Camera Installation Package</h2>
    <p class="list-head">Includes:</p>
    <ul class="list">
      <li>Conduct a site survey and explain installation</li>
      <li>Unpack Your Camera/DVR system</li>
      <li>Mount and Secure your Cameras</li>
      <li>Conceal Wiring from mount to DVR viewing room</li>
      <li>Program Basic functions on the DVR</li>
      <li>Tutorial on basic features of your new system</li>
      <li>Clean up work area and remove installation debris</li>
    </ul>
    <p class="list-head">Does not Includes:</p>
    <ul class="list">
      <li>Equipment or wiring</li>
      <li>Network Set-up for remote Viewing ($100 additional)</li>
    </ul>
  </section>

  <section class="panel panel-full">
    <h2 class="package-title">4 Camera Installation with Equipment</h2>
    <p class="list-head">Includes:</p>
    <ul class="list">
      <li>Conduct a site survey and explain installation</li>
      <li>Mount and Secure your Cameras</li>
      <li>Conceal Wiring from mount to DVR viewing room</li>
      <li>Program Basic functions on the DVR</li>
      <li>Tutorial on basic features of your new system</li>
      <li>Clean up work area and remove installation debris</li>
      <li>4 night vision/color cameras</li>
      <li>4 sets of 60ft connection cables (.30c per foot after)</li>
      <li>4 Channel Digital Video Recorder</li>
    </ul>
    <p class="list-head">Does not includes:</p>
    <ul class="list">
      <li>Viewing monitor</li>
      <li>Network Set-up for remote Viewing ($100 additional)</li>
    </ul>
  </section>
</div>
</body>
</html>
```